Tailbrook Website Design

Need a website for a Dog Grooiming business. Please make it simular to these:

https://www.furvanto.com
https://haulnorix.com
https://meadowpetrin.com
https://www.drivelumo.com/search/

```html
<!DOCTYPE html>
<html lang="en">
<head>
<meta charset="utf-8">
<title>Tailbrook – About</title>
<link href="https://fonts.googleapis.com/css2?family=Montserrat:wght@600;700;800&family=Open+Sans:wght@400;600&display=swap" rel="stylesheet">
<style>
:root{
  --purple:#8b3c9e;
  --ink:#222326;
  --text:#5c5d61;
  --muted:#8a8b8f;
  --paper:#ffffff;
  --mist:#f1f1f2;
  --night:#1f1f21;
  --night-line:#3a3a3d;
}
*{margin:0;padding:0;box-sizing:border-box}
html,body{width:677px;height:1200px;overflow:hidden;background:var(--paper)}
body{font-family:"Open Sans",Arial,sans-serif;color:var(--text);position:relative}
.page{position:relative;width:677px;height:1200px;overflow:hidden}
h1,h2,h3,.brand,.nav a{font-family:"Montserrat",Arial,sans-serif}

/* header */
.site-header{position:absolute;top:0;left:0;width:677px;height:62px;background:var(--paper)}
.brand{position:absolute;left:22px;top:17px;font-size:21px;font-weight:800;color:var(--ink);letter-spacing:.3px;text-transform:uppercase}
.top-contacts{position:absolute;right:22px;top:9px;display:flex;gap:22px;font-size:10px;color:var(--ink)}
.top-contacts span{display:flex;align-items:center;gap:5px}
.top-contacts b{font-size:12px;font-weight:600}
.top-contacts svg{width:10px;height:10px;fill:var(--purple)}
.nav{position:absolute;right:22px;top:36px;display:flex;gap:16px}
.nav a{font-size:9.5px;font-weight:600;color:var(--ink);text-decoration:none;text-transform:uppercase;padding-bottom:5px}
.nav a.active{color:var(--purple);border-bottom:2px solid var(--purple)}

/* hero */
.hero{position:absolute;top:62px;left:0;width:677px;height:255px}
.hero-photo{position:absolute;inset:0;background:linear-gradient(90deg,#2e2e30 0%,#5a5553 35%,#9b8a7c 60%,#c98f52 78%,#7a5d4a 100%)}
.hero h1{position:absolute;left:60px;top:150px;color:#fff;font-size:38px;font-weight:700}
.hero-curve{position:absolute;left:0;bottom:-1px;width:677px;height:50px}

/* about */
.about{position:absolute;top:330px;left:0;width:677px}
.about h2{position:absolute;left:60px;top:16px;font-size:22px;font-weight:700;color:var(--ink);text-transform:uppercase}
.about p{position:absolute;left:60px;width:280px;font-size:9.6px;line-height:15px}
.about .p1{top:54px}
.about .p2{top:110px}
.about-photo{position:absolute;left:375px;top:12px;width:240px;height:195px;border-radius:8px;background:linear-gradient(135deg,#8fb4cc 0%,#c7a07a 45%,#d4863b 65%,#9fb7c9 100%)}

/* team */
.team{position:absolute;top:575px;left:0;width:677px;height:400px;background:var(--mist)}
.team-curve{position:absolute;top:-1px;left:0;width:677px;height:40px}
.team h2{position:absolute;top:60px;width:100%;text-align:center;font-size:22px;font-weight:700;color:var(--ink);text-transform:uppercase}
.arrow{position:absolute;top:168px;width:14px;height:14px;stroke:var(--muted);fill:none;stroke-width:2}
.arrow.prev{left:14px}.arrow.next{right:14px}
.member{position:absolute;top:110px;width:130px;text-align:center}
.portrait{width:124px;height:124px;margin:0 auto;border-radius:50%;border:3px solid #bdbdbf;background:linear-gradient(180deg,#e9e9ea,#9c9c9f)}
.member.featured .portrait{border-color:var(--purple)}
.member h3{margin-top:14px;font-size:15px;font-weight:600;color:var(--ink)}
.member .role{font-size:9px;color:var(--muted);text-transform:uppercase;margin-top:2px}
.member p{font-size:9.4px;line-height:14px;margin-top:6px;padding:0 8px}
.member a{display:block;margin-top:10px;font-family:"Montserrat",Arial,sans-serif;font-size:9px;font-weight:700;color:var(--purple);text-decoration:none}

/* footer */
.site-footer{position:absolute;top:940px;left:0;width:677px;height:260px}
.footer-bg{position:absolute;inset:0;width:677px;height:260px}
.footer-brand{position:absolute;left:60px;top:115px;font-size:21px;font-weight:800;color:#fff;text-transform:uppercase}
.footer-col{position:absolute;top:62px;color:#d9d9db}
.footer-col h4{font-family:"Montserrat",Arial,sans-serif;font-size:11px;font-weight:700;color:#fff;text-transform:uppercase;margin-bottom:12px}
.links{display:grid;grid-template-columns:84px 90px;row-gap:3px;font-size:9.5px}
.quick{left:245px}
.contact{left:455px}
.contact-row{display:flex;gap:7px;font-size:9.5px;line-height:13px;margin-bottom:13px;width:170px}
.contact-row svg{flex:none;width:10px;height:10px;fill:#fff;margin-top:2px}
.footer-rule{position:absolute;left:22px;right:22px;top:222px;height:1px;background:var(--night-line)}
.copyright{position:absolute;left:22px;top:238px;font-size:9px;color:#cfcfd1}
.social{position:absolute;right:22px;top:232px;display:flex;gap:8px}
.social span{width:20px;height:20px;border-radius:50%;border:1px solid #8a8a8d}
</style>
</head>
<body>
<div class="page">

<header class="site-header">
  <div class="brand">Tailbrook</div>
  <div class="top-contacts">
    <span><svg viewBox="0 0 24 24"><path d="M6.6 10.8a15 15 0 0 0 6.6 6.6l2.2-2.2a1 1 0 0 1 1-.3 11.4 11.4 0 0 0 3.6.6 1 1 0 0 1 1 1V20a1 1 0 0 1-1 1A17 17 0 0 1 3 4a1 1 0 0 1 1-1h3.5a1 1 0 0 1 1 1 11.4 11.4 0 0 0 .6 3.6 1 1 0 0 1-.3 1z"/></svg>Call us <b>1 800 555 0142</b></span>
    <span><svg viewBox="0 0 24 24"><path d="M2 5h20v14H2zm2 2v.5l8 5 8-5V7z"/></svg>Email us <b>hello@tailbrook.com</b></span>
  </div>
  <nav class="nav">
    <a href="#">Home</a><a href="#" class="active">About</a><a href="#">Locations</a><a href="#">Careers</a><a href="#">Blog</a><a href="#">Contact</a>
  </nav>
</header>

<section class="hero">
  <div class="hero-photo" role="img" aria-label="Happy dog with a red collar after grooming, dimmed on the left"></div>
  <h1>ABOUT</h1>
  <svg class="hero-curve" viewBox="0 0 677 50" preserveAspectRatio="none"><path d="M0 50 Q338 -10 677 50 Z" fill="#fff"/></svg>
</section>

<section class="about">
  <h2>About Tailbrook</h2>
  <p class="p1">Lorem ipsum dolor sit amet, consectetur adipiscing elit, sed do eiusmod tempor incididunt ut labore.</p>
  <p class="p2">Sed et dolore magna aliqua. Ut enim ad minim veniam, quis nostrud exercitation ullamco laboris nisi ut aliquip ex ea commodo consequat. Duis aute irure dolor in reprehenderit in voluptate velit esse cillum dolore eu fugiat nulla pariatur. Excepteur sint occaecat cupidatat non proident sunt in culpa qui officia deserunt mollit anim id est labor.</p>
  <div class="about-photo" role="img" aria-label="Groomer brushing a fluffy small dog"></div>
</section>

<section class="team">
  <svg class="team-curve" viewBox="0 0 677 40" preserveAspectRatio="none"><path d="M0 0 H677 V30 Q338 -18 0 30 Z" fill="#fff"/></svg>
  <h2>Meet the Team</h2>
  <svg class="arrow prev" viewBox="0 0 14 14"><path d="M9 2 4 7l5 5"/></svg>
  <svg class="arrow next" viewBox="0 0 14 14"><path d="M5 2l5 5-5 5"/></svg>

  <div class="member" style="left:62px">
    <div class="portrait" role="img" aria-label="Portrait of team member John Doe"></div>
    <h3>John Doe</h3><div class="role">CEO</div>
    <p>Lorem ipsum dolor sit amet, consectetur adipiscing elit, sed do eiusm</p>
    <a href="#">READ MORE</a>
  </div>
  <div class="member featured" style="left:201px">
    <div class="portrait" role="img" aria-label="Portrait of team member Clara"></div>
    <h3>Clara</h3><div class="role">CEO</div>
    <p>Lorem ipsum dolor sit amet, consectetur adipiscing elit, sed do eiusm</p>
    <a href="#">READ MORE</a>
  </div>
  <div class="member" style="left:340px">
    <div class="portrait" role="img" aria-label="Portrait of team member Henry"></div>
    <h3>Henry</h3><div class="role">CEO</div>
    <p>Lorem ipsum dolor sit amet, consectetur adipiscing elit, sed do eiusm</p>
    <a href="#">READ MORE</a>
  </div>
  <div class="member" style="left:479px">
    <div class="portrait" role="img" aria-label="Portrait of team member Agnes"></div>
    <h3>Agnes</h3><div class="role">CEO</div>
    <p>Lorem ipsum dolor sit amet, consectetur adipiscing elit, sed do eiusm</p>
    <a href="#">READ MORE</a>
  </div>
</section>

<footer class="site-footer">
  <svg class="footer-bg" viewBox="0 0 677 260" preserveAspectRatio="none"><path d="M0 30 Q338 -20 677 30 V260 H0 Z" fill="#1f1f21"/></svg>
  <div class="footer-brand">Tailbrook</div>
  <div class="footer-col quick">
    <h4>Quick Links</h4>
    <div class="links">
      <span>Home</span><span>Terms of Service</span>
      <span>About</span><span>Privacy Policy</span>
      <span>Locations</span><span>Book Online</span>
      <span>Careers</span><span></span>
      <span>Blog</span><span></span>
      <span>Contact</span><span></span>
    </div>
  </div>
  <div class="footer-col contact">
    <h4>Contact Us</h4>
    <div class="contact-row"><svg viewBox="0 0 24 24"><path d="M12 2a7 7 0 0 0-7 7c0 5 7 13 7 13s7-8 7-13a7 7 0 0 0-7-7zm0 9.5A2.5 2.5 0 1 1 12 6.5a2.5 2.5 0 0 1 0 5z"/></svg><span>No 1 Elm Street, Suite 4, Springfield Area</span></div>
    <div class="contact-row"><svg viewBox="0 0 24 24"><path d="M6.6 10.8a15 15 0 0 0 6.6 6.6l2.2-2.2a1 1 0 0 1 1-.3 11.4 11.4 0 0 0 3.6.6 1 1 0 0 1 1 1V20a1 1 0 0 1-1 1A17 17 0 0 1 3 4a1 1 0 0 1 1-1h3.5a1 1 0 0 1 1 1 11.4 11.4 0 0 0 .6 3.6 1 1 0 0 1-.3 1z"/></svg><span>1 800 555 0142</span></div>
    <div class="contact-row"><svg viewBox="0 0 24 24"><path d="M2 5h20v14H2zm2 2v.5l8 5 8-5V7z"/></svg><span>hello@tailbrook.com</span></div>
  </div>
  <div class="footer-rule"></div>
  <div class="copyright">© 2021, Tailbrook. All rights reserved.</div>
  <div class="social"><span></span><span></span><span></span></div>
</footer>

</div>
</body>
</html>
```